Window and GutterCleaning Flyer A5 size double sided.

We need a double sided A5 flyer. Side 1, is for window cleaning, side 2 is for gutter cleaning. Licensed by Borough of Calderwick Authority.
Phone number 0800 471 3926.
Business address 17 Fenmarrow Loan, West Brankholm Edinburgh EH47 3TP.
www.bright-pane-services.example
We use a LoftOrb Gutter inspection Cam to view your gutters first to see if they need doing.
Window cleaning ; Professional window cleaning services, what we offer, water fed pole window cleaning able to reach windows up to 60 feet.
Conservatory cleaning.
Conservatory roof cleaning.
Fascias & Soffits cleaning.
Excellent Customer Service.
Target Market(s)
domestic houses
Industry/Entity Type
window cleaning
Look and feel
Each slider illustrates characteristics of the customer's brand and the style your logo design should communicate.

```html
<!DOCTYPE html>
<html lang="en">
<head>
<meta charset="utf-8">
<title>Bright Pane Services – A5 Flyer</title>
<link href="https://fonts.googleapis.com/css2?family=Quicksand:wght@500;600;700&family=Roboto+Condensed:wght@400&family=Roboto:wght@400&display=swap" rel="stylesheet">
<style>
:root{
  --sky:#a8cbea;
  --navy:#2b2a6b;
  --ink:#2f2f3a;
  --paper:#ffffff;
  --stage:#e9e6e2;
}
*{box-sizing:border-box;margin:0;padding:0}
html,body{width:1200px;height:861px;overflow:hidden;background:var(--stage)}
.stage{position:absolute;left:0;top:0;width:1418px;height:1018px;transform:scale(.8463);transform-origin:0 0}
.flyer{position:absolute;top:72px;width:620px;height:875px;background:var(--paper);overflow:hidden;font-family:"Quicksand",sans-serif;color:var(--ink)}
.flyer--front{left:63px}
.flyer--back{left:736px}
.abs{position:absolute}
.header-band{left:0;top:0;width:620px;height:175px}
.brand{left:28px;top:40px;display:flex;align-items:center;gap:10px;color:var(--navy);font-weight:700;font-size:25px;line-height:1.05}
.brand__mark{width:18px;height:18px;background:var(--navy)}
.contact-head{right:33px;top:38px;text-align:right;color:var(--navy)}
.contact-head__label{font-size:17px;font-weight:500}
.contact-head__phone{display:flex;align-items:center;justify-content:flex-end;gap:8px;margin-top:6px;font-family:"Roboto Condensed",sans-serif;font-size:42px;line-height:1}
.front-copy{left:20px;top:188px;width:580px;color:var(--navy)}
.front-copy__lead{font-size:17px;font-weight:600;line-height:26px}
.front-copy h3{font-size:15px;font-weight:700;margin-top:14px}
.front-copy p{font-size:12.5px;line-height:20px;color:var(--ink);font-weight:500;margin-top:2px}
.photo{position:absolute}
.footer-band{left:0;top:700px;width:620px;height:175px}
.footer-brand{left:0;width:620px;top:740px;display:flex;justify-content:center;align-items:center;gap:8px;color:var(--navy);font-weight:700;font-size:20px}
.footer-brand__mark{width:12px;height:12px;background:var(--navy)}
.footer-info{left:0;width:620px;font-family:"Roboto",sans-serif;font-size:14px;color:var(--navy);display:flex;justify-content:center;align-items:center;gap:26px}
.footer-info span{display:inline-flex;align-items:center;gap:7px}
.back-intro{left:16px;top:184px;width:590px;font-size:12px;line-height:19px;font-weight:500}
.offer-title{left:19px;top:250px;font-size:17px;font-weight:600;color:var(--navy)}
.service{position:absolute;top:448px;width:196px;text-align:center;font-family:"Roboto",sans-serif;font-size:17px;line-height:21px;color:var(--navy)}
.why{left:17px;top:515px;color:var(--navy)}
.why h2{font-size:25px;font-weight:700}
.why ul{list-style:none;margin-top:8px}
.why li{font-size:14.5px;font-weight:600;color:#222;line-height:28px}
.why li::before{content:"• "}
.cta{left:225px;top:792px;font-family:"Roboto",sans-serif;font-size:15.5px;line-height:21.5px;color:var(--navy)}
</style>
</head>
<body>
<div class="stage">

  <!-- FRONT: window cleaning -->
  <section class="flyer flyer--front">
    <svg class="abs header-band" viewBox="0 0 620 175" aria-hidden="true">
      <rect width="620" height="175" fill="#a8cbea"/>
      <path d="M0 162 Q160 145 320 158 T620 150 L620 175 L0 175Z" fill="#fff"/>
    </svg>
    <div class="abs brand"><span class="brand__mark"></span><span>Bright Pane<br>Services</span></div>
    <div class="abs contact-head">
      <div class="contact-head__label">For More Information Contact Us</div>
      <div class="contact-head__phone">
        <svg width="42" height="42" viewBox="0 0 42 42" aria-hidden="true"><circle cx="21" cy="21" r="19" fill="none" stroke="#2b2a6b" stroke-width="2.5"/><path d="M15 10c-3 2-4 5-2 10 2 5 5 9 9 11 3 1 5 0 6-2l-3-4-3 2c-2-1-4-4-5-7l2-2-4-8z" fill="#2b2a6b"/></svg>
        0800 471 3926
      </div>
    </div>

    <div class="abs front-copy">
      <div class="front-copy__lead">Crystal Clear Views, Every Time! Fully licensed by Borough of Calderwick Authority for your complete peace of mind.</div>
      <h3>Professional Window Cleaning Services.</h3>
      <p>We offer high-quality window cleaning for domestic homes, delivering spotless, streak-free results every time with a friendly, reliable service you can count on, week after week.</p>
      <h3>Pure Water Fed Pole System.</h3>
      <p>Our advanced system reaches up to 60 feet high, safely cleaning upper windows from the ground without the need for ladders.</p>
    </div>

    <div class="photo" role="img" aria-label="Water fed brush spraying a window pane" style="left:0;top:425px;width:185px;height:360px;background:linear-gradient(160deg,#7c9ab5,#c2d4e0 55%,#8aa3b8)"></div>
    <div class="photo" role="img" aria-label="Red brick house front with white windows" style="left:190px;top:425px;width:153px;height:360px;background:linear-gradient(180deg,#9a5a44,#b9795c 60%,#d9d0c2)"></div>
    <div class="photo" role="img" aria-label="Water fed pole cleaning a white framed window" style="left:350px;top:425px;width:270px;height:360px;background:linear-gradient(135deg,#e9eeef,#a9b3b6 60%,#6e7779)"></div>

    <svg class="abs footer-band" viewBox="0 0 620 175" aria-hidden="true">
      <path d="M0 90 L310 18 L620 90 L620 175 L0 175Z" fill="#a8cbea"/>
      <path d="M0 78 L310 8 L620 78 L620 90 L310 22 L0 90Z" fill="#2b2a6b"/>
    </svg>
    <div class="abs footer-brand"><span class="footer-brand__mark"></span>Bright Pane Services</div>
    <div class="abs footer-info" style="top:810px">
      <span><svg width="14" height="18" viewBox="0 0 14 18" aria-hidden="true"><path d="M7 0a7 7 0 0 0-7 7c0 5 7 11 7 11s7-6 7-11a7 7 0 0 0-7-7zm0 10a3 3 0 1 1 0-6 3 3 0 0 1 0 6z" fill="#2b2a6b"/></svg>17 Fenmarrow Loan, West Brankholm, Edinburgh EH47 3TP</span>
    </div>
    <div class="abs footer-info" style="top:836px;font-size:13px">
      <span><svg width="20" height="14" viewBox="0 0 20 14" aria-hidden="true"><rect x="1" y="1" width="18" height="12" rx="2" fill="none" stroke="#2b2a6b" stroke-width="2"/><path d="M1 2l9 6 9-6" fill="none" stroke="#2b2a6b" stroke-width="2"/></svg>info@bright-pane-services.example</span>
      <span><svg width="18" height="18" viewBox="0 0 18 18" aria-hidden="true"><circle cx="9" cy="9" r="8" fill="none" stroke="#2b2a6b" stroke-width="1.6"/><ellipse cx="9" cy="9" rx="3.5" ry="8" fill="none" stroke="#2b2a6b" stroke-width="1.4"/><path d="M1 9h16M2.5 5h13M2.5 13h13" stroke="#2b2a6b" stroke-width="1.2"/></svg>www.bright-pane-services.example</span>
    </div>
  </section>

  <!-- BACK: gutter cleaning -->
  <section class="flyer flyer--back">
    <svg class="abs header-band" viewBox="0 0 620 175" aria-hidden="true">
      <rect width="620" height="175" fill="#a8cbea"/>
      <path d="M0 162 Q160 145 320 158 T620 150 L620 175 L0 175Z" fill="#fff"/>
    </svg>
    <div class="abs brand"><span class="brand__mark"></span><span>Bright Pane<br>Services</span></div>
    <div class="abs contact-head">
      <div class="contact-head__label">For More Information Contact Us</div>
      <div class="contact-head__phone">
        <svg width="42" height="42" viewBox="0 0 42 42" aria-hidden="true"><circle cx="21" cy="21" r="19" fill="none" stroke="#2b2a6b" stroke-width="2.5"/><path d="M15 10c-3 2-4 5-2 10 2 5 5 9 9 11 3 1 5 0 6-2l-3-4-3 2c-2-1-4-4-5-7l2-2-4-8z" fill="#2b2a6b"/></svg>
        0800 471 3926
      </div>
    </div>

    <p class="abs back-intro">Gutters are an important part of your home. We use a LoftOrb Gutter Inspection Cam to view your gutters first to see if they need doing. So why not set up an annual plan &amp; make sure you don't run into problems when winter comes.</p>
    <div class="abs offer-title">We Also Offer</div>

    <div class="photo" role="img" aria-label="White conservatory on a brick house" style="left:0;top:281px;width:195px;height:151px;background:linear-gradient(180deg,#cfdbe4,#e8ecee 55%,#a0644c)"></div>
    <div class="photo" role="img" aria-label="Dirty conservatory roof panels" style="left:212px;top:281px;width:195px;height:151px;background:linear-gradient(160deg,#8d8f7a,#b6bcb5 50%,#d7dcdf)"></div>
    <div class="photo" role="img" aria-label="House eaves with gutter, fascia and soffit marked by arrows" style="left:424px;top:281px;width:196px;height:151px;background:linear-gradient(180deg,#f2f3f3,#d9dcdd 55%,#9c6250)"></div>

    <div class="service" style="left:0">Conservatory<br>Cleaning</div>
    <div class="service" style="left:212px">Conservatory<br>Roof Cleaning</div>
    <div class="service" style="left:424px">Fascias And<br>Soffits Cleaning</div>

    <div class="abs why">
      <h2>Why Choose Us?</h2>
      <ul>
        <li>Friendly, Professional Service</li>
        <li>Reliable And Efficient</li>
        <li>Fully Licensed And Insured</li>
        <li>Excellent Customer Satisfaction</li>
      </ul>
    </div>

    <svg class="abs footer-band" viewBox="0 0 620 175" aria-hidden="true">
      <path d="M0 90 L300 25 L620 90 L620 175 L0 175Z" fill="#a8cbea"/>
      <path d="M0 85 L300 14 L620 78 L620 88 L300 26 L0 90Z" fill="#2b2a6b"/>
    </svg>
    <div class="photo" role="img" aria-label="Rugged gutter inspection camera tablet showing a modern house" style="left:300px;top:515px;width:310px;height:250px;border-radius:18px;background:linear-gradient(135deg,#3a3d42,#1f2226 50%,#4d6a86)"></div>
    <div class="photo" role="img" aria-label="Smiling customer adviser at a laptop" style="left:28px;top:665px;width:170px;height:210px;border-radius:60px 60px 0 0;background:linear-gradient(180deg,#e8d3a8,#f3ece4 45%,#dfe9f4)"></div>

    <div class="abs cta">Contact Us<br>For A Free No Obligation Quote To Clear<br>Them Out And Get Them Working As They Should.</div>
  </section>

</div>
</body>
</html>
```